Design wine label. Brand name The Quillmere

Wine label design for 'The Quillmere'. A few varieties but example-

The Quillmere Shiraz 2016 Bendigo 750ml, 14%alc/vol.

'The quillmere' at top of label, image of sparrow then vintage, variety etc under image.

simple, yet striking and modern look.

Font styles to use
Script

Requirements
Must have
• Image of a sparrow
Nice to have
• Simple image, outline, cartoon or Lino print style. Some colour but not too busy

```html
<!DOCTYPE html>
<html lang="en">
<head>
<meta charset="utf-8">
<title>The Quillmere – Shiraz 2016 Bendigo</title>
<link rel="stylesheet" href="https://fonts.googleapis.com/css2?family=Pinyon+Script&display=swap">
<style>
  :root {
    --paper: #ffffff;
    --label-black: #0d0d0d;
    --gold-light: #f6e08a;
    --gold-mid: #d9ae3c;
    --gold-dark: #8a6414;
    --sky-light: #eef5fc;
    --sky-mid: #a9cdf0;
    --sky-deep: #5f9fdc;
    --ink: #111111;
    --bird-light: #a47a40;
    --bird-dark: #5a3a16;
  }
  html, body {
    margin: 0;
    padding: 0;
    overflow: hidden;
    background: var(--paper);
  }
  .canvas {
    position: relative;
    width: 1200px;
    height: 1200px;
    overflow: hidden;
    background: var(--paper);
    font-family: "Pinyon Script", cursive;
  }
  .label-art {
    position: absolute;
    inset: 0;
    width: 1200px;
    height: 1200px;
  }
  .brand {
    position: absolute;
    left: 0;
    width: 1200px;
    text-align: center;
    margin: 0;
    font-weight: 400;
    background: linear-gradient(180deg, var(--gold-light) 0%, var(--gold-mid) 55%, var(--gold-dark) 100%);
    -webkit-background-clip: text;
    background-clip: text;
    color: transparent;
  }
  .brand-article {
    top: 135px;
    font-size: 72px;
    line-height: 1;
  }
  .brand-name {
    top: 225px;
    font-size: 150px;
    line-height: 1;
  }
  .wine-details {
    position: absolute;
    top: 612px;
    left: 0;
    width: 1200px;
    margin: 0;
    text-align: center;
    font-size: 72px;
    line-height: 1;
    color: var(--ink);
    font-weight: 400;
  }
  .bird-illustration {
    position: absolute;
    left: 413px;
    top: 695px;
    width: 360px;
    height: 340px;
    background: linear-gradient(150deg, var(--bird-light) 0%, var(--bird-dark) 100%);
    opacity: 0.8;
  }
  .bottle-facts {
    position: absolute;
    top: 1040px;
    left: 265px;
    width: 660px;
    display: flex;
    justify-content: space-between;
    font-size: 62px;
    line-height: 1;
    color: var(--ink);
  }
</style>
</head>
<body>
<main class="canvas">
  <svg class="label-art" viewBox="0 0 1200 1200" aria-hidden="true">
    <defs>
      <radialGradient id="sky" cx="50%" cy="45%" r="70%">
        <stop offset="0%" stop-color="var(--sky-light)"/>
        <stop offset="45%" stop-color="var(--sky-mid)"/>
        <stop offset="100%" stop-color="var(--sky-deep)"/>
      </radialGradient>
      <linearGradient id="gold-line" x1="0" y1="0" x2="1" y2="1">
        <stop offset="0%" stop-color="var(--gold-light)"/>
        <stop offset="50%" stop-color="var(--gold-mid)"/>
        <stop offset="100%" stop-color="var(--gold-dark)"/>
      </linearGradient>
    </defs>
    <path class="label-outline" fill="var(--label-black)"
      d="M213,1152 V240 Q240,240 240,212 C300,212 330,170 330,118 C460,118 520,30 598,30 C676,30 736,118 866,118 C866,170 896,212 957,212 Q957,240 984,240 V1152 Z"/>
    <path class="sky-field" fill="url(#sky)"
      d="M228,383 C330,383 400,470 450,520 C500,565 550,578 598,578 C646,578 696,565 746,520 C796,470 866,383 969,383 V1137 H228 Z"/>
    <path class="frame-rule" fill="none" stroke="url(#gold-line)" stroke-width="4"
      d="M252,362 V252 Q268,252 268,234 C318,234 352,196 352,150 C470,150 530,66 598,66 C666,66 726,150 844,150 C844,196 878,234 928,234 Q928,252 944,252 V362 C850,362 790,440 740,492 C690,540 650,552 598,552 C546,552 506,540 456,492 C406,440 346,362 252,362 Z"/>
    <path class="frame-rule" fill="none" stroke="url(#gold-line)" stroke-width="2.5"
      d="M266,350 V264 Q280,264 280,248 C330,248 366,210 366,164 C478,164 536,82 598,82 C660,82 718,164 830,164 C830,210 866,248 916,248 Q916,264 930,264 V350 C842,350 780,428 730,480 C682,526 644,538 598,538 C552,538 514,526 466,480 C416,428 354,350 266,350 Z"/>
  </svg>

  <h1 class="brand brand-article">The</h1>
  <p class="brand brand-name">Quillmere</p>

  <h2 class="wine-details">Shiraz 2016 Bendigo</h2>

  <div class="bird-illustration" role="img" aria-label="Illustration of four bronze sparrows in flight"></div>

  <div class="bottle-facts">
    <span class="volume">750 ml</span>
    <span class="alcohol">14% alc/vol</span>
  </div>
</main>
</body>
</html>
```